Stylish Homeware business needs a Logo and Business Card design

We need a logo and business card for a new company based in Hong Kong called "Nest Lumora". We do marketing and distributing international curated goods for calm living rooms. Products we handle included clocks, picture frame, small kitchen wares, LED lightenings, stationary and etc. We planned to also create our own brands next step. We could like to see designs that use pastel colors. The final design shoudl be simple and stylish.
Target Market(s)
Asia, Mainly Japan, China and Korea
Industry/Entity Type
Business
Contact Information for Business Card
We could like to see designs that use pastel colors. The final design shoudl be simple and stylish. We attach some log design we like on the bottom of the page.
Font styles to use
Look and feel
Each slider illustrates characteristics of the customer's brand and the style your logo design should communicate.

```html
<!DOCTYPE html>
<html lang="en">
<head>
<meta charset="utf-8">
<title>Nest Lumora – Business Card</title>
<link href="https://fonts.googleapis.com/css2?family=Roboto:wght@400;500;700&display=swap" rel="stylesheet">
<style>
  :root {
    --page-bg: #ecebe8;
    --card-bg: #ffffff;
    --accent-blue: #6b84c8;
    --accent-pink: #ee86b5;
    --ink: #2f2f33;
    --muted: #7b7b80;
    --rule: #c9c9cc;
    --shadow: rgba(40, 35, 30, 0.16);
  }
  * { box-sizing: border-box; margin: 0; padding: 0; }
  html, body { width: 1200px; height: 800px; overflow: hidden; }
  body {
    background: var(--page-bg);
    font-family: "Roboto", sans-serif;
    color: var(--ink);
    position: relative;
  }
  .card {
    position: absolute;
    top: 250px;
    width: 520px;
    height: 300px;
    background: var(--card-bg);
    border-radius: 4px;
    box-shadow: 0 10px 28px var(--shadow);
  }
  .card--back { left: 50px; }
  .card--front { left: 630px; display: flex; align-items: center; justify-content: center; }

  .brand__name {
    display: flex;
    align-items: center;
    gap: 10px;
    font-size: 32px;
    font-weight: 500;
    color: var(--ink);
    white-space: nowrap;
  }
  .brand__mark {
    width: 14px; height: 14px;
    border-radius: 50%;
    background: var(--muted);
    flex: none;
  }
  .brand__tagline {
    margin-top: 6px;
    padding-left: 24px;
    font-size: 13px;
    color: var(--muted);
    letter-spacing: 0.3px;
  }

  .card--back .brand {
    position: absolute;
    left: 30px;
    top: 118px;
  }
  .card--back .brand__name { font-size: 25px; gap: 8px; }
  .card--back .brand__mark { width: 11px; height: 11px; }
  .card--back .brand__tagline { font-size: 10.5px; padding-left: 19px; }

  .divider {
    position: absolute;
    left: 262px;
    top: 80px;
    width: 1px;
    height: 140px;
    background: var(--rule);
  }

  .contact {
    position: absolute;
    left: 284px;
    top: 74px;
  }
  .contact__name {
    font-size: 21px;
    font-weight: 700;
    letter-spacing: 1px;
    text-transform: uppercase;
  }
  .contact__role {
    font-size: 13px;
    color: var(--accent-blue);
    margin-top: 2px;
  }
  .contact__address {
    font-size: 13px;
    line-height: 17px;
    margin-top: 8px;
  }
  .contact__list { list-style: none; margin-top: 8px; }
  .contact__item {
    display: flex;
    align-items: center;
    gap: 7px;
    font-size: 13px;
    line-height: 18px;
  }
  .contact__icon { width: 11px; height: 11px; flex: none; }
</style>
</head>
<body>

  <section class="card card--back" aria-label="Business card, contact side">
    <div class="brand">
      <div class="brand__name"><span class="brand__mark"></span>Nest Lumora</div>
      <div class="brand__tagline">curated goods for calm living rooms</div>
    </div>

    <div class="divider"></div>

    <div class="contact">
      <div class="contact__name">Mara Ellison</div>
      <div class="contact__role">Director Operations</div>
      <div class="contact__address">418 Linden Row<br>Harbor City 40517</div>
      <ul class="contact__list">
        <li class="contact__item">
          <svg class="contact__icon" viewBox="0 0 12 12" aria-hidden="true"><rect x="3" y="0.8" width="6" height="10.4" rx="1.2" fill="none" stroke="var(--accent-pink)" stroke-width="1.3"/></svg>
          041-552-908
        </li>
        <li class="contact__item">
          <svg class="contact__icon" viewBox="0 0 12 12" aria-hidden="true"><path d="M2.5 1 L4.6 1 L5.4 3.6 L4.1 4.6 C4.8 6 5.9 7.2 7.4 7.9 L8.4 6.6 L11 7.4 L11 9.5 C11 10.3 10.3 11 9.5 11 C5.3 10.6 1.4 6.7 1 2.5 C1 1.7 1.7 1 2.5 1 Z" fill="var(--accent-pink)"/></svg>
          236-781-420
        </li>
        <li class="contact__item">
          <svg class="contact__icon" viewBox="0 0 12 12" aria-hidden="true"><rect x="0.8" y="2.2" width="10.4" height="7.6" rx="1" fill="var(--accent-pink)"/><path d="M1.2 2.8 L6 6.4 L10.8 2.8" fill="none" stroke="#fff" stroke-width="1.1"/></svg>
          mara@nestlumora.com
        </li>
        <li class="contact__item">
          <svg class="contact__icon" viewBox="0 0 12 12" aria-hidden="true"><rect x="0.8" y="1.6" width="10.4" height="7.2" rx="1" fill="none" stroke="var(--accent-pink)" stroke-width="1.2"/><line x1="4" y1="10.8" x2="8" y2="10.8" stroke="var(--accent-pink)" stroke-width="1.2"/></svg>
          www.nestlumora.com
        </li>
      </ul>
    </div>
  </section>

  <section class="card card--front" aria-label="Business card, brand side">
    <div class="brand">
      <div class="brand__name"><span class="brand__mark"></span>Nest Lumora</div>
      <div class="brand__tagline">curated goods for calm living rooms</div>
    </div>
  </section>

</body>
</html>
```